PEACFUL ACUPUNCTURE PRACTITIONER NEEDS A NEW COAT

I need a new design for an exiting website http://willowgateneedlework.com/ for a acupuncturist. This will be a minimalism design with lots and lots of white space. Home page and one interior page. Please keep the feeling of calm and peaceful serenity. For Color scheme: https://www.morningfernclinic.com/fertility. The bottom part of the home page with sections and links to the service pages: https://harborlotuswellness.com/. The client likes this the best: http://mfclinic.com/. I'm attaching the logo and content pages.

Target Market(s)

Women

Industry/Entity Type

Wellness, health, wellbeing, meditation

Number of Pages Required

2 page

Font styles to use
Sans Serif
Decorative

Colors

Designer to choose colors to be used in the design.

Requirements
Must have
Nice to have
• Follow new website drafts and links
Should not have
• Busy with bright colors. No poping

```html
<!DOCTYPE html>
<html lang="en">
<head>
<meta charset="utf-8">
<title>Willow Gate Acupuncture</title>
<link rel="stylesheet" href="https://fonts.googleapis.com/css2?family=Josefin+Sans:wght@300;400;600&display=swap">
<style>
  :root {
    --mauve: #b5848a;
    --slate: #a9b6c5;
    --ink: #3a3335;
    --card: #f6f4f4;
    --rule: #ebe7e7;
    --white: #ffffff;
  }
  * { margin: 0; padding: 0; box-sizing: border-box; }
  html, body { width: 818px; height: 1200px; overflow: hidden; background: var(--white); }
  body { font-family: "Josefin Sans", sans-serif; color: var(--ink); position: relative; }

  .topbar { position: absolute; top: 0; left: 0; width: 818px; height: 25px; background: var(--slate); }
  .topbar__email { position: absolute; left: 110px; top: 9px; font-size: 7px; color: var(--white); font-weight: 400; }

  .brand { position: absolute; top: 25px; left: 0; width: 818px; height: 57px; border-bottom: 1px solid var(--rule);
    display: flex; align-items: center; justify-content: center; gap: 6px; }
  .brand__dot { width: 14px; height: 14px; border-radius: 50%; background: var(--mauve); opacity: .7; }
  .brand__name { font-size: 14px; color: #5a5254; font-weight: 400; letter-spacing: .3px; }

  .nav { position: absolute; top: 82px; left: 110px; width: 598px; height: 38px; display: flex; justify-content: space-between; align-items: center; }
  .nav a { font-size: 8.6px; color: #4a4345; text-decoration: none; font-weight: 300; letter-spacing: .3px; }

  .hero { position: absolute; top: 120px; left: 0; width: 818px; height: 485px; }
  .hero__photo { position: absolute; inset: 0;
    background: linear-gradient(100deg, #ede4e1 0%, #eedfd6 38%, #ecccb4 62%, #dfa77e 85%, #c98a5f 100%); }
  .hero__title { position: absolute; left: 112px; top: 134px; font-size: 34px; line-height: 40px; font-weight: 600; color: var(--mauve); }
  .hero__text { position: absolute; left: 111px; top: 232px; width: 350px; font-size: 10.2px; line-height: 18.5px; font-weight: 300; color: var(--ink); }
  .hero__button { position: absolute; left: 110px; top: 314px; width: 89px; height: 33px; border-radius: 17px; background: var(--slate);
    color: var(--white); font-size: 7.8px; font-weight: 400; display: flex; align-items: center; justify-content: center; letter-spacing: .3px; }

  .section-title { position: absolute; left: 0; width: 818px; text-align: center; font-size: 28px; font-weight: 400; color: var(--mauve); letter-spacing: .6px; }
  .philosophy__title { top: 652px; }
  .philosophy__text { position: absolute; left: 110px; width: 598px; text-align: center; font-size: 9.3px; line-height: 17.4px; font-weight: 300; }
  .philosophy__text--first { top: 703px; }
  .philosophy__text--second { top: 753px; }

  .divider { position: absolute; top: 835px; left: 110px; width: 598px; height: 1px; background: var(--rule); }

  .focus__title { top: 884px; }
  .focus__cards { position: absolute; top: 946px; left: 110px; width: 598px; display: flex; justify-content: space-between; }
  .focus-card { width: 138px; height: 169px; background: var(--card); display: flex; flex-direction: column; align-items: center; }
  .focus-card__icon { margin-top: 40px; width: 44px; height: 44px; display: block; }
  .focus-card__icon--placeholder { border-radius: 50%; background: #dde2ea; }
  .focus-card__label { margin-top: 20px; text-align: center; font-size: 12.5px; line-height: 16px; font-weight: 300; color: var(--mauve); letter-spacing: .3px; }

  .footer { position: absolute; top: 1166px; left: 0; width: 818px; height: 34px; background: var(--slate);
    display: flex; align-items: center; justify-content: center; }
  .footer__text { font-size: 7.6px; color: var(--white); font-weight: 400; }
</style>
</head>
<body>
  <div class="topbar"><span class="topbar__email">nora@willowgateneedlework.com</span></div>

  <header class="brand">
    <span class="brand__dot"></span>
    <span class="brand__name">Willow Gate Acupuncture</span>
  </header>

  <nav class="nav">
    <a href="#">Home</a>
    <a href="#">About</a>
    <a href="#">Fertility &amp; Pregnancy</a>
    <a href="#">Hormone Balance</a>
    <a href="#">Strength &amp; Structure</a>
    <a href="#">Emotional Wellbeing</a>
    <a href="#">Online Shop</a>
    <a href="#">Testimonials</a>
  </nav>

  <section class="hero">
    <div class="hero__photo" role="img" aria-label="Close-up photo of a practitioner's hands placing acupuncture needles in a patient's shoulder, soft warm light"></div>
    <h1 class="hero__title">Welcome To<br>Willow Gate</h1>
    <p class="hero__text">Lorem ipsum dolor sit amet, consectetur adipiscing elit, sed do mod eiusmod tempor incididunt ut labore et dolore magna aliqua nisi ut et aliquip ex ea commodo consequat.</p>
    <div class="hero__button">CONTACT US</div>
  </section>

  <h2 class="section-title philosophy__title">Philosophy of Care</h2>
  <p class="philosophy__text philosophy__text--first">Acupuncture &amp; Chinese Herbal Medicine are rooted in over 3000 years of history and tradition. As a complete medical system that has remained flexible and relevant we honor what has worked from the past while embracing the medicine of tomorrow.</p>
  <p class="philosophy__text philosophy__text--second">At Willow Gate Acupuncture we provide compassionate, respectful and empowering care in a safe &amp;inclusive environment. Our goal is to harmonize physical, mental and emotionalwellbeing to strengthen the Willow Gate from which we all strive to live.</p>

  <div class="divider"></div>

  <h2 class="section-title focus__title">Areas of Focus</h2>
  <div class="focus__cards">
    <div class="focus-card">
      <span class="focus-card__icon focus-card__icon--placeholder" role="img" aria-label="Line illustration of eggs in a nest"></span>
      <div class="focus-card__label">Fertility &amp;<br>Pregnancy</div>
    </div>
    <div class="focus-card">
      <span class="focus-card__icon focus-card__icon--placeholder" role="img" aria-label="Line illustration of stacked balancing stones"></span>
      <div class="focus-card__label">Hormone<br>Balance</div>
    </div>
    <div class="focus-card">
      <span class="focus-card__icon focus-card__icon--placeholder" role="img" aria-label="Line illustration of a tree"></span>
      <div class="focus-card__label">Strength &amp;<br>Structure</div>
    </div>
    <div class="focus-card">
      <svg class="focus-card__icon" viewBox="0 0 44 44" aria-hidden="true">
        <path d="M22 40 C12 30 3 23 3 13 C3 6 8 3 13 3 C17 3 20 5 22 9 C24 5 27 3 31 3 C36 3 41 6 41 13 C41 23 32 30 22 40 Z" fill="none" stroke="#a9b6c5" stroke-width="1.6" stroke-linejoin="round"/>
      </svg>
      <div class="focus-card__label">Emotional<br>Well-Being</div>
    </div>
  </div>

  <footer class="footer">
    <span class="footer__text">Copyright © 2021 Willow Gate Acupuncture | 14 Alder Row | Easthaven MA. 555-014-2286. All Rights Reserved.</span>
  </footer>
</body>
</html>
```